Corporate Brightfen business cards to be handed to investor, bankers etc. Needs to have a young feel

I need business cards designed for a technology company that provides uber-like rapid response on the security industry. I would like it simple but very cool and tasteful. See attached documents for artwork and colours to be used. Cut sheet describes business model. Card stock should be thicker than normal. I would like the one side to be just the art and the other to have the contact info with maybe the pin somewhere.

Target Market(s)

Investors

Industry/Entity Type

Business

Contact Information for Business Card

Would like the logo attached on one side with name address and other info on the other side.

Font styles to use
Other font styles liked:
• See existing logo

Colors
6b449b
886aae
e4daeb
ffffff

Requirements
Must have
• Name: Dorian Felkatsis
• Address: 47 Larkfield Avenue, Toronto, On, M6K2B7
• Tel: 416-7291846
• Email: rolo@brightfen.io
Nice to have
• See logo colours

```html
<!DOCTYPE html>
<html lang="en">
<head>
<meta charset="utf-8">
<title>Brightfen Business Cards</title>
<link href="https://fonts.googleapis.com/css2?family=Lato:wght@300;400&display=swap" rel="stylesheet">
<style>
  :root {
    --purple-deep: #6b449b;
    --purple: #7b5ea0;
    --purple-light: #886aae;
    --lavender: #e4daeb;
    --white: #ffffff;
    --ink: #222222;
    --stage: #232323;
  }
  * { margin: 0; padding: 0; box-sizing: border-box; }
  html, body {
    width: 1200px; height: 801px; overflow: hidden;
    background: var(--stage);
    font-family: "Lato", sans-serif;
  }
  .sheet {
    position: relative; width: 1200px; height: 801px;
    display: flex; align-items: center; justify-content: center; gap: 60px;
  }
  .card {
    position: relative; width: 520px; height: 297px;
    border-radius: 4px; overflow: hidden;
    box-shadow: 0 14px 40px rgba(0,0,0,.45);
  }
  /* front: contact side */
  .card--front { background: var(--white); }
  .card--front .brand {
    position: absolute; left: 44px; top: 92px;
    display: flex; align-items: center; gap: 8px;
  }
  .brand__dot {
    width: 22px; height: 22px; border-radius: 50%;
    background: var(--purple-deep);
  }
  .brand__name {
    font-weight: 300; font-size: 54px; line-height: 1;
    letter-spacing: -1px; color: var(--ink);
  }
  .holder-name {
    position: absolute; left: 96px; top: 196px;
    font-size: 21px; font-weight: 400; color: var(--purple);
  }
  .contact {
    position: absolute; left: 336px; top: 96px;
    font-size: 13px; font-weight: 400; color: var(--ink); line-height: 1.35;
  }
  .contact__address { margin-bottom: 14px; }
  .contact__row { display: flex; align-items: center; gap: 7px; }
  .contact__row svg { width: 10px; height: 10px; fill: var(--purple); flex: none; }
  .card__band {
    position: absolute; left: 0; right: 0; bottom: 0; height: 12px;
    background: var(--purple);
  }
  /* back: brand side */
  .card--back {
    background: var(--purple);
    display: flex; align-items: center; justify-content: center;
  }
  .card--back .brand { display: flex; align-items: center; gap: 10px; }
  .card--back .brand__dot { background: var(--white); width: 26px; height: 26px; }
  .card--back .brand__name { color: var(--white); font-size: 66px; }
</style>
</head>
<body>
<main class="sheet">
  <section class="card card--front" aria-label="Business card, contact side">
    <div class="brand">
      <span class="brand__dot"></span>
      <span class="brand__name">brightfen</span>
    </div>
    <p class="holder-name">Dorian Felkatsis</p>
    <address class="contact" style="font-style:normal">
      <div class="contact__address">47 Larkfield Avenue<br>Toronto, On, M6K2B7</div>
      <div class="contact__row">
        <svg viewBox="0 0 24 24" aria-hidden="true"><path d="M6.6 10.8a15.1 15.1 0 0 0 6.6 6.6l2.2-2.2c.3-.3.7-.4 1-.2 1.1.4 2.3.6 3.6.6.6 0 1 .4 1 1V20c0 .6-.4 1-1 1A17 17 0 0 1 3 4c0-.6.4-1 1-1h3.5c.6 0 1 .4 1 1 0 1.3.2 2.5.6 3.6.1.3 0 .7-.2 1z"/></svg>
        <span>416-7291846</span>
      </div>
      <div class="contact__row">
        <svg viewBox="0 0 24 24" aria-hidden="true"><path d="M2 5h20v14H2zm2 2v.5l8 5 8-5V7zm0 2.8V17h16V9.8l-8 5z"/></svg>
        <span>rolo@brightfen.io</span>
      </div>
    </address>
    <div class="card__band"></div>
  </section>

  <section class="card card--back" aria-label="Business card, brand side">
    <div class="brand">
      <span class="brand__dot"></span>
      <span class="brand__name">brightfen</span>
    </div>
  </section>
</main>
</body>
</html>
```